logo for a full service car wash and detail center
Briar Glen Suds & Shine ,Car Wash & Detail Center
logo for a full service car wash and detail center - Automotive
Creative Brief
Bright & Fun-filled
Nate Ferrando
General Manager
412 Harbrook blvd Corwin Bay TN 31872
Nate.briarglensuds@examplemail.com

```html
<!DOCTYPE html>
<html lang="en">
<head>
<meta charset="utf-8">
<title>Briar Glen Suds &amp; Shine – Business Card</title>
<link rel="stylesheet" href="https://fonts.googleapis.com/css2?family=Open+Sans:wght@400;600;700&display=swap">
<style>
  :root {
    --backdrop: #8a8c8e;
    --card: #ffffff;
    --brand-blue: #2a8fd8;
    --brand-blue-light: #5cb8ee;
    --ink: #5a5d60;
    --ink-dark: #3d4044;
  }
  * { margin: 0; padding: 0; box-sizing: border-box; }
  html, body {
    width: 1200px; height: 908px; overflow: hidden;
    background: var(--backdrop);
    font-family: "Open Sans", Arial, sans-serif;
  }
  .card {
    position: absolute;
    left: 170px; top: 209px;
    width: 860px; height: 490px;
    background: var(--card);
    border-radius: 22px;
    overflow: hidden;
  }
  .card__swoosh { position: absolute; inset: 0; }
  .holder {
    position: absolute; right: 160px; top: 110px;
    text-align: right;
  }
  .holder__name {
    font-size: 28px; font-weight: 600; color: var(--ink-dark); line-height: 1.15;
  }
  .holder__title {
    font-size: 22px; font-weight: 700; color: var(--brand-blue); line-height: 1.2;
  }
  .brand {
    position: absolute; left: 60px; top: 215px;
    display: flex; align-items: center; gap: 16px;
  }
  .brand__dot {
    width: 46px; height: 46px; border-radius: 50%;
    background: var(--brand-blue-light);
    flex: none;
  }
  .brand__name {
    font-size: 36px; font-weight: 700; color: var(--brand-blue); line-height: 1.1;
  }
  .brand__tagline {
    position: absolute; left: 122px; top: 265px;
    font-size: 15px; font-weight: 600; letter-spacing: 2px;
    text-transform: uppercase; color: var(--brand-blue);
  }
  .contact {
    position: absolute; left: 60px; top: 340px;
    font-size: 17px; color: var(--ink); line-height: 1.45;
  }
  .contact__row { display: flex; align-items: center; gap: 8px; }
  .contact__icon { width: 18px; height: 18px; flex: none; }
</style>
</head>
<body>
  <div class="card">
    <svg class="card__swoosh" width="860" height="490" viewBox="0 0 860 490" aria-hidden="true">
      <defs>
        <linearGradient id="blueBand" x1="0" y1="0" x2="1" y2="1">
          <stop offset="0" stop-color="#5cb8ee"/>
          <stop offset="1" stop-color="#1f7fcc"/>
        </linearGradient>
        <linearGradient id="steelBand" x1="0" y1="0" x2="1" y2="1">
          <stop offset="0" stop-color="#f1f2f3"/>
          <stop offset="0.6" stop-color="#b5b9bd"/>
          <stop offset="1" stop-color="#8d9297"/>
        </linearGradient>
      </defs>
      <path d="M600 40 C720 80 815 170 860 320 V120 C800 80 700 50 600 40 Z" fill="url(#steelBand)"/>
      <path d="M470 0 H860 V150 C780 80 640 25 470 0 Z" fill="url(#blueBand)"/>
    </svg>

    <div class="holder">
      <p class="holder__name">Nate Ferrando</p>
      <p class="holder__title">General Manager</p>
    </div>

    <div class="brand">
      <span class="brand__dot"></span>
      <span class="brand__name">Briar Glen Suds &amp; Shine</span>
    </div>
    <p class="brand__tagline">Car Wash &amp; Detail Center</p>

    <div class="contact">
      <p>412 Harbrook blvd</p>
      <p>Corwin Bay TN 31872</p>
      <p class="contact__row">
        <svg class="contact__icon" viewBox="0 0 20 20" aria-hidden="true">
          <circle cx="10" cy="10" r="9" fill="none" stroke="#5a5d60" stroke-width="1.6"/>
          <path d="M7 5.5 L8.6 5.5 L9.4 8 L8.3 8.9 C8.9 10.3 9.8 11.2 11.1 11.8 L12 10.7 L14.5 11.5 L14.5 13 C11 13.5 6.5 9.5 7 5.5 Z" fill="#5a5d60"/>
        </svg>
        555-201-0172
      </p>
      <p class="contact__row">
        <svg class="contact__icon" viewBox="0 0 20 20" aria-hidden="true">
          <circle cx="10" cy="10" r="9" fill="none" stroke="#5a5d60" stroke-width="1.6"/>
          <rect x="5" y="6.5" width="10" height="7" rx="1" fill="none" stroke="#5a5d60" stroke-width="1.4"/>
          <path d="M5 7 L10 11 L15 7" fill="none" stroke="#5a5d60" stroke-width="1.4"/>
        </svg>
        Nate.briarglensuds@examplemail.com
      </p>
    </div>
  </div>
</body>
</html>
```